Corwick Habitat Web

We just need an update/re-design of our existing web site that would include our new company logo and some new photo's. Our current web site can be viewed at www.corwickhabitat.com.au. We would require something very similar to what we have at the moment in terms of content it should all be the same.
The web site would basically act more as a portfolio than one that would generate more business.
We are after a very modern and simple design and maybe something where we can upload our own project photo's and project descriptions as we complete them.

Industry/Entity Type

It Company

```html
<!DOCTYPE html>
<html lang="en">
<head>
<meta charset="utf-8">
<title>Corwick Habitat</title>
<link rel="stylesheet" href="https://fonts.googleapis.com/css2?family=PT+Sans:wght@400;700&family=Arimo:wght@400;700&display=swap">
<style>
:root{
  --ink:#3a3d47;
  --panel:#353a48;
  --card-btn:#4a4c60;
  --accent:#c0272d;
  --paper:#ffffff;
  --footer-bg:#ececec;
  --muted:#6b6d74;
  --sky-light:#e8f3fa;
  --sky:#a9d0e6;
  --glass:#2f7f93;
  --bronze:#3e2a1c;
}
*{box-sizing:border-box;margin:0;padding:0}
html,body{width:1200px;height:1170px;overflow:hidden}
body{position:relative;background:var(--paper);font-family:"PT Sans",sans-serif;color:var(--ink)}

.hero{position:absolute;left:0;top:0;width:1200px;height:459px;
  background:linear-gradient(100deg,var(--sky) 0%,var(--sky-light) 30%,#cfe6ef 45%,var(--glass) 68%,#1f5364 82%,var(--bronze) 100%)}
.topbar{position:absolute;left:0;top:0;width:1200px;height:69px;background:rgba(255,255,255,.55)}
.brand{position:absolute;left:303px;top:0;width:180px;height:69px;background:var(--paper);
  display:flex;align-items:center;justify-content:center;font-size:19px;color:#6e6e72;letter-spacing:.3px;white-space:nowrap}
.main-nav{position:absolute;left:570px;top:28px;font-size:11px;color:#2d2d33;display:flex;gap:6px;text-transform:uppercase;white-space:nowrap}
.main-nav .sep{color:#777}
.main-nav .active{border-bottom:2px solid var(--accent);padding-bottom:3px}

.hero-title{position:absolute;left:453px;top:225px;width:295px;height:64px;background:rgba(60,60,62,.9);
  color:#fff;font-family:"Arimo",sans-serif;font-weight:700;font-size:27px;text-align:center;line-height:58px;letter-spacing:-.3px;white-space:nowrap}
.hero-btn{position:absolute;left:522px;top:278px;width:157px;height:24px;background:var(--paper);
  font-family:"Arimo",sans-serif;font-size:11.5px;color:#333;text-align:center;line-height:24px;white-space:nowrap}

.projects{position:absolute;left:312px;top:402px;display:flex;gap:5px}
.project-card{width:140px;height:277px;background:var(--paper);border:1px solid #e6e6e6;position:relative}
.project-photo{height:103px}
.project-name{position:absolute;left:14px;top:130px;font-weight:400;font-size:10.5px;line-height:11px;color:#333;text-transform:uppercase;white-space:nowrap}
.project-text{position:absolute;left:14px;top:166px;width:115px;font-size:7px;line-height:10.6px;color:#555}
.more-btn{position:absolute;left:-1px;bottom:-1px;width:140px;height:34px;
  background:linear-gradient(100deg,var(--card-btn) 0%,#3c3f52 45%,#8a7d78 70%,#5b5668 100%);
  color:#fff;font-family:"Arimo",sans-serif;font-size:8.5px;display:flex;align-items:center;padding-left:16px;gap:9px;white-space:nowrap}

.about{position:absolute;left:312px;top:690px;width:575px;height:272px;background:var(--panel);color:#e9eaee}
.about h2{position:absolute;left:21px;top:24px;font-weight:400;font-size:17px;line-height:18px;letter-spacing:.4px;white-space:nowrap}
.about .intro{position:absolute;left:21px;top:75px;width:280px;font-size:8.5px;line-height:11px}
.about .rule{position:absolute;left:21px;width:274px;height:1px;background:#4c5162}
.about .lead{position:absolute;left:21px;top:141px;font-size:10.5px;white-space:nowrap}
.services{position:absolute;left:21px;top:169px;list-style:none;display:grid;grid-template-columns:135px 120px;row-gap:8px;font-size:9.5px}
.services li{display:flex;align-items:center;gap:6px;height:14px;white-space:nowrap}
.about .more{position:absolute;left:230px;top:248px;font-family:"Arimo",sans-serif;font-size:8.5px;display:flex;gap:8px;align-items:center;white-space:nowrap}
.about-photo{position:absolute;left:323px;top:8px;width:244px;height:253px}

.footer{position:absolute;left:0;top:1009px;width:1200px;height:161px;background:var(--footer-bg)}
.footer-brand{position:absolute;left:529px;top:985px;width:141px;height:57px;background:#3d3d3f;border:3px solid #b9b9bb;
  color:#e4e4e4;font-size:15px;display:flex;align-items:center;justify-content:center;white-space:nowrap}
.footer-nav{position:absolute;left:0;top:1072px;width:1200px;display:flex;justify-content:center;gap:6px;font-size:10.5px;color:#333;text-transform:uppercase;white-space:nowrap}
.copyright{position:absolute;left:0;top:1100px;width:1200px;text-align:center;font-family:"Arimo",sans-serif;font-size:7.5px;color:#444}
</style>
</head>
<body>

<div class="hero" role="img" aria-label="Upward view of glass office towers against a pale sky"></div>
<header class="topbar"></header>
<div class="brand">Corwick Habitat</div>
<nav class="main-nav">
  <span>Home</span><span class="sep">·</span>
  <span>About Us</span><span class="sep">·</span>
  <span class="active">Recent Projects</span><span class="sep">·</span>
  <span>Our Services</span><span class="sep">·</span>
  <span>Contact Us</span>
</nav>

<h1 class="hero-title">Multi Storey Offices</h1>
<div class="hero-btn">BROWSE OUR PROJECTS</div>

<section class="projects">
  <article class="project-card">
    <div class="project-photo" role="img" aria-label="Close-up of timber slice wall panels" style="background:linear-gradient(90deg,#3a2414,#b98a5c 40%,#6b4426 70%,#c99b6a)"></div>
    <h3 class="project-name">Harlow Freight<br>Distribution Centre</h3>
    <p class="project-text">Lorem Ipsum is simply dummy text of the printing and typesetting industry. Lorem Ipsum has been the industry's standard dummy tscrambled.</p>
    <a class="more-btn"><svg width="9" height="9" viewBox="0 0 9 9"><rect x="0.5" y="0.5" width="8" height="8" fill="none" stroke="#fff"/><path d="M2 4.5h4M4.5 2.5l2 2-2 2" fill="none" stroke="#fff"/></svg>More Details</a>
  </article>
  <article class="project-card">
    <div class="project-photo" role="img" aria-label="Open two-level car showroom interior" style="background:linear-gradient(180deg,#2a2d33,#9aa4ad 55%,#d9dde0)"></div>
    <h3 class="project-name">Veltro Motors<br>Alexandria</h3>
    <p class="project-text">Lorem Ipsum is simply dummy text of the printing and typesetting industry. Lorem Ipsum has been the industry's standard dummy tscrambled.</p>
    <a class="more-btn"><svg width="9" height="9" viewBox="0 0 9 9"><rect x="0.5" y="0.5" width="8" height="8" fill="none" stroke="#fff"/><path d="M2 4.5h4M4.5 2.5l2 2-2 2" fill="none" stroke="#fff"/></svg>More Details</a>
  </article>
  <article class="project-card">
    <div class="project-photo" role="img" aria-label="Modern building facade with red frame" style="background:linear-gradient(180deg,#dfe6ec,#a34a3a 45%,#8f8a86 75%,#c9c5bf)"></div>
    <h3 class="project-name">Harlow Freight<br>Distribution Centre</h3>
    <p class="project-text">Lorem Ipsum is simply dummy text of the printing and typesetting industry. Lorem Ipsum has been the industry's standard dummy tscrambled.</p>
    <a class="more-btn"><svg width="9" height="9" viewBox="0 0 9 9"><rect x="0.5" y="0.5" width="8" height="8" fill="none" stroke="#fff"/><path d="M2 4.5h4M4.5 2.5l2 2-2 2" fill="none" stroke="#fff"/></svg>More Details</a>
  </article>
  <article class="project-card">
    <div class="project-photo" role="img" aria-label="Office lobby with timber ceiling" style="background:linear-gradient(180deg,#2b2b30,#9a6a3e 35%,#d8d6d0 70%,#8a7a5a)"></div>
    <h3 class="project-name">Harlow Freight<br>Distribution Centre</h3>
    <p class="project-text">Lorem Ipsum is simply dummy text of the printing and typesetting industry. Lorem Ipsum has been the industry's standard dummy tscrambled.</p>
    <a class="more-btn"><svg width="9" height="9" viewBox="0 0 9 9"><rect x="0.5" y="0.5" width="8" height="8" fill="none" stroke="#fff"/><path d="M2 4.5h4M4.5 2.5l2 2-2 2" fill="none" stroke="#fff"/></svg>More Details</a>
  </article>
</section>

<section class="about">
  <h2>CORWICK<br>HABITAT PTY LTD</h2>
  <p class="intro">Corwick Habitat Pty Ltd was established in 2005 and has been operating in the Sydney area, but has completed numerous projects outside of Sydney.</p>
  <div class="rule" style="top:126px"></div>
  <p class="lead">We specialise in the internal fit outs to,</p>
  <ul class="services">
    <li><svg width="11" height="11" viewBox="0 0 11 11"><circle cx="5.5" cy="5.5" r="5.5" fill="#c9ccd3"/><path d="M3 5.6l1.8 1.8L8 4" fill="none" stroke="#353a48" stroke-width="1.4"/></svg>Industrial Offices</li>
    <li><svg width="11" height="11" viewBox="0 0 11 11"><circle cx="5.5" cy="5.5" r="5.5" fill="#c9ccd3"/><path d="M3 5.6l1.8 1.8L8 4" fill="none" stroke="#353a48" stroke-width="1.4"/></svg>Residential Houses</li>
    <li><svg width="11" height="11" viewBox="0 0 11 11"><circle cx="5.5" cy="5.5" r="5.5" fill="#c9ccd3"/><path d="M3 5.6l1.8 1.8L8 4" fill="none" stroke="#353a48" stroke-width="1.4"/></svg>Multi Storey Offices</li>
    <li><svg width="11" height="11" viewBox="0 0 11 11"><circle cx="5.5" cy="5.5" r="5.5" fill="#c9ccd3"/><path d="M3 5.6l1.8 1.8L8 4" fill="none" stroke="#353a48" stroke-width="1.4"/></svg>External Facades</li>
    <li><svg width="11" height="11" viewBox="0 0 11 11"><circle cx="5.5" cy="5.5" r="5.5" fill="#c9ccd3"/><path d="M3 5.6l1.8 1.8L8 4" fill="none" stroke="#353a48" stroke-width="1.4"/></svg>Commercial Projects</li>
  </ul>
  <div class="rule" style="top:243px"></div>
  <a class="more"><svg width="9" height="9" viewBox="0 0 9 9"><rect x="0.5" y="0.5" width="8" height="8" fill="none" stroke="#fff"/><path d="M2 4.5h4M4.5 2.5l2 2-2 2" fill="none" stroke="#fff"/></svg>More Details</a>
  <div class="about-photo" role="img" aria-label="Office foyer with timber slat ceiling and lift lobby" style="background:linear-gradient(180deg,#e9eaea 0%,#3a3a3e 18%,#9b6a3f 35%,#dcdad4 60%,#8a857c 88%,#4a3a2a 100%)"></div>
</section>

<footer class="footer"></footer>
<div class="footer-brand">Corwick Habitat</div>
<nav class="footer-nav">
  <span>Home</span><span>·</span><span>About Us</span><span>·</span><span>Recent Projects</span><span>·</span><span>Our Services</span><span>·</span><span>Contact Us</span>
</nav>
<p class="copyright">© Copyright Corwick Habitat Pty Ltd 2013</p>

</body>
</html>
```